Redesign business card for Wade Linford Construction

Basically I want a complete redesign of the business card I have attached with this project. The only stipulations I have are that the colors , crimson and white, stay the same and all of the information on the old card is also on the new design. Also I would like to add that we also specialize in metal building foundations as well. I look forward to seeing what you all come up with.
Industry/Entity Type
Business
Contact Information for Business Card
All of the details are on the attachment I have included with this project
Look and feel
Each slider illustrates characteristics of the customer's brand and the style your logo design should communicate.

```html
<!DOCTYPE html>
<html lang="en">
<head>
<meta charset="utf-8">
<title>Wade Linford Construction – Business Card</title>
<link rel="stylesheet" href="https://fonts.googleapis.com/css2?family=Ubuntu:wght@400;500;700&display=swap">
<style>
  :root {
    --crimson: #ef4452;
    --crimson-deep: #e62a38;
    --white: #ffffff;
    --paper: #fbfbfb;
    --backdrop: #2e2e30;
  }
  * { margin: 0; padding: 0; box-sizing: border-box; }
  html, body {
    width: 1200px; height: 1000px; overflow: hidden;
    background: var(--backdrop);
    font-family: "Ubuntu", sans-serif;
  }
  .card {
    position: absolute;
    width: 770px; height: 440px;
    left: 215px;
    background: linear-gradient(135deg, var(--crimson) 0%, var(--crimson-deep) 100%);
    overflow: hidden;
  }
  .card--back { top: 40px; }
  .card--front { top: 520px; }

  /* Back */
  .back-mark {
    position: absolute; left: 50%; top: 50%;
    transform: translate(-50%, -50%);
    display: flex; align-items: center; gap: 22px;
    color: var(--white);
    white-space: nowrap;
  }
  .back-mark__circle { flex: none; width: 70px; height: 70px; border-radius: 50%; background: var(--white); }
  .back-mark__name { font-size: 46px; font-weight: 700; letter-spacing: 0.5px; }

  /* Front: white panel */
  .founder-panel {
    position: absolute; left: 0; top: 0; bottom: 0; width: 280px;
    background: var(--paper);
    color: var(--crimson);
    text-align: center;
    padding-top: 50px;
  }
  .brand-mark { display: flex; flex-direction: column; align-items: center; gap: 10px; }
  .brand-mark__circle { width: 46px; height: 46px; border-radius: 50%; background: var(--crimson); }
  .brand-mark__name { font-size: 22px; font-weight: 700; white-space: nowrap; }
  .founder-role { margin-top: 26px; font-size: 19px; }
  .founder-name { font-size: 26px; font-weight: 700; margin-top: 2px; white-space: nowrap; }
  .founder-nick { font-size: 19px; margin-top: 2px; }
  .founder-address {
    position: absolute; left: 34px; bottom: 40px;
    text-align: left; font-size: 19px; line-height: 1.35;
    white-space: nowrap;
  }

  /* Front: contact block */
  .contact {
    position: absolute; right: 34px; top: 30px; left: 300px;
    color: var(--white); text-align: right;
  }
  .contact__company { font-size: 25px; font-weight: 700; white-space: nowrap; }
  .contact__trade { font-size: 18px; margin-top: 2px; }
  .contact__person { font-size: 24px; font-weight: 700; margin-top: 14px; }
  .contact__title { font-size: 18px; margin-top: 2px; }
  .contact__lines { margin-top: 14px; font-size: 18px; font-weight: 500; line-height: 1.4; white-space: nowrap; }
  .contact__services {
    margin-top: 14px; font-size: 15.5px; line-height: 1.4; text-align: right;
  }
</style>
</head>
<body>
  <section class="card card--back" aria-label="Card back">
    <div class="back-mark">
      <span class="back-mark__circle"></span>
      <span class="back-mark__name">Wade Linford</span>
    </div>
  </section>

  <section class="card card--front" aria-label="Card front">
    <div class="founder-panel">
      <div class="brand-mark">
        <span class="brand-mark__circle"></span>
        <span class="brand-mark__name">Wade Linford</span>
      </div>
      <p class="founder-role">Founder</p>
      <p class="founder-name">Wade Linford</p>
      <p class="founder-nick">“CURBHAWK”</p>
      <p class="founder-address">418 Birch Hollow Rd.<br>Fairview, AL 36099</p>
    </div>

    <div class="contact">
      <p class="contact__company">Wade Linford Construction</p>
      <p class="contact__trade">Concrete Contractor</p>
      <p class="contact__person">Wade J. Linford</p>
      <p class="contact__title">Owner</p>
      <div class="contact__lines">
        <p>Business: 555- 014- 2290</p>
        <p>Mobile: 555- 014- 2291</p>
        <p>Home: 555- 016- 7384</p>
        <p>Email: office.wadelinford@example.com</p>
      </div>
      <p class="contact__services">Specializing in concrete foundations, driveways, storm rooms additions and most other forms of concrete work we also specialize in metal building foundations as well</p>
    </div>
  </section>
</body>
</html>
```